High School Senior Ad for annual

My son is a senior, and we bought an Ad for the back of the annual and looking for a one page Ad that meets the below specification. We have to submit out final Ad by Monday 11/07/22.

Specifications:
- Must be a JPEG @ 300 DPI.
- Full page size is 8.667 inches wide by 11.333 inches tall, or 2600 pixels by 3400 pixels.
- Do NOT take wording to the edge. Leave at least ½ inch on all sides without wording.

What we want:
- Looking for a creative artistic use of the photo we provide
- His name Tobin Halvik should be in a very artistic script at the top
- Insert the attached bible verse and text somewhere on the Ad
- I'm attaching some examples of some that we like along with the photos that we want to use. Please look at the instruction doc to understand what we are looking for.
- If you have questions, please ask

```html
<!DOCTYPE html>
<html lang="en">
<head>
<meta charset="utf-8">
<title>Tobin Halvik – Senior Ad</title>
<link href="https://fonts.googleapis.com/css2?family=Allura&family=Poppins:wght@400;500;600&display=swap" rel="stylesheet">
<style>
  :root {
    --backdrop: #a4a4a6;
    --night: #0c1118;
    --navy: #0f2350;
    --navy-deep: #0a1a3e;
    --gate-dark: #2a3038;
    --gate-grey: #7d848d;
    --pavement: #c9ccd1;
    --brick: #8a4a3c;
    --white: #ffffff;
    --panel: rgba(255,255,255,0.22);
    --hair: #e0cd8e;
    --skin: #e6c2aa;
    --shirt-blue: #a9bde0;
    --blazer: #1b2c58;
    --khaki: #c7b593;
    --golf-green: #4f7a3a;
    --field-gold: #9a8a3e;
    --flag-red: #c44a4e;
  }
  * { margin: 0; padding: 0; box-sizing: border-box; }
  html, body { width: 720px; height: 1200px; overflow: hidden; }
  body { background: var(--backdrop); position: relative; font-family: "Poppins", sans-serif; }

  .ad-page {
    position: absolute; left: 30px; top: 168px;
    width: 660px; height: 863px; overflow: hidden;
    background: var(--night);
    box-shadow: 0 4px 14px rgba(0,0,0,0.35);
  }

  /* background scene behind the senior: iron gate, pavement, brick */
  .gate-scene {
    position: absolute; inset: 0;
    background:
      linear-gradient(180deg, rgba(12,17,24,0.9) 0%, rgba(12,17,24,0) 9%),
      linear-gradient(180deg, transparent 60%, rgba(201,204,209,0.55) 78%, rgba(185,188,194,0.7) 100%),
      linear-gradient(90deg, var(--gate-dark) 0%, var(--gate-grey) 22%, #959ba3 40%, var(--gate-grey) 62%, #6f6a6a 80%, var(--brick) 100%);
  }

  /* main portrait subject area */
  .portrait-subject {
    position: absolute; left: 165px; top: 150px; width: 345px; height: 713px;
    background: linear-gradient(180deg,
      var(--hair) 0%, var(--hair) 7%,
      var(--skin) 11%, var(--skin) 22%,
      var(--shirt-blue) 27%, var(--shirt-blue) 34%,
      var(--blazer) 40%, var(--navy) 72%,
      var(--khaki) 86%, #b9a886 100%);
    -webkit-mask-image: radial-gradient(ellipse 62% 70% at 50% 52%, #000 72%, transparent 100%);
            mask-image: radial-gradient(ellipse 62% 70% at 50% 52%, #000 72%, transparent 100%);
  }

  .name-script {
    position: absolute; left: 0; width: 100%; top: 6px;
    text-align: center;
    font-family: "Allura", cursive; font-weight: 400;
    font-size: 92px; line-height: 1; color: var(--white);
    padding-right: 10px;
  }
  .name-swoosh { position: absolute; left: 0; top: 0; }
  .verse {
    position: absolute; left: 0; width: 100%; top: 125px;
    text-align: center;
    font-weight: 500; font-size: 13px; letter-spacing: 1.2px;
    word-spacing: 2px; color: var(--white);
  }
  .verse .ref { margin-left: 18px; }

  .message-circle { position: absolute; left: 0; top: 0; }

  .message {
    position: absolute; left: 40px; width: 304px; top: 600px;
    text-align: center; color: var(--white);
    font-size: 8.6px; line-height: 11px;
  }
  .message p + p { margin-top: 9px; }
  .signoff {
    display: block; margin: 4px 0 5px;
    font-size: 15px; line-height: 18px;
    font-variant: small-caps; letter-spacing: 0.5px;
  }
  .signoff.sibling { font-size: 13px; margin: 4px 0 0; }

  .thumb-strip {
    position: absolute; left: 502px; top: 173px; width: 142px; height: 652px;
    background: var(--panel);
  }
  .thumb {
    position: absolute; left: 10px; width: 122px; height: 150px;
    border: 2px solid var(--white);
  }
  .thumb.golf { top: 19px; background: linear-gradient(180deg, #4e6a3e 0%, #7a8a5a 40%, var(--golf-green) 70%, #3f6430 100%); }
  .thumb.steps { top: 180px; background: linear-gradient(160deg, #8b6a5a 0%, #c9cdd3 35%, var(--shirt-blue) 60%, #b9a98a 100%); }
  .thumb.soccer { top: 341px; background: radial-gradient(circle at 50% 45%, #d9b46a 0%, var(--field-gold) 45%, #3d7a42 100%); }
  .thumb.flagwall { top: 490px; background: linear-gradient(180deg, #3a4f8a 0%, var(--flag-red) 30%, #e8d7d0 55%, var(--flag-red) 75%, #5a5e66 100%); }
</style>
</head>
<body>
  <main class="ad-page">
    <div class="gate-scene" role="img" aria-label="Blurred iron gate and brick building behind the senior"></div>
    <div class="portrait-subject" role="img" aria-label="Senior portrait of Tobin in a navy blazer, light blue shirt and striped tie, leaning on the gate"></div>

    <h1 class="name-script">Tobin Halvik</h1>
    <svg class="name-swoosh" width="660" height="863" aria-hidden="true">
      <path d="M180 109 Q310 103 458 106" stroke="#fff" stroke-width="2.2" fill="none" stroke-linecap="round"/>
    </svg>
    <p class="verse">Behold, children are a gift from the Lord....<span class="ref">Psalm 127:3</span></p>

    <svg class="message-circle" width="660" height="863" aria-hidden="true">
      <defs>
        <linearGradient id="circleFill" x1="0" y1="0" x2="0" y2="1">
          <stop offset="0" stop-color="#12295c" stop-opacity="0.93"/>
          <stop offset="1" stop-color="#0a1a3e" stop-opacity="0.97"/>
        </linearGradient>
      </defs>
      <circle cx="190" cy="815" r="262" fill="url(#circleFill)"/>
      <circle cx="206" cy="826" r="272" fill="none" stroke="#fff" stroke-opacity="0.7" stroke-width="0.8"/>
    </svg>

    <div class="message">
      <p>Tobin, you are a blessing from the Lord, and we are so thankful for you. You have brought so much joy and love into our lives. It has been an honor to watch you grow into an amazing, kind, intelligent, and hard-working young man. We have loved every minute of watching you play golf for RCS. Your strong work ethic during golf season was inspiring. We are so proud of you, and we are excited to see the wonderful plans God has for your life. We will always be here to love, support, and encourage you. We hope you never outgrow your love of travel, history, and a good book!</p>
      <p>Remember, “The more that you read, the more things that you will know. The more that you learn, the more places you’ll go!” – A. Whitlow</p>
      <span class="signoff">Love, MOM &amp; DAD</span>
      <p>Tobin, Congrats on graduating! I hope you enjoyed your senior year as much as I did. Good luck at Lakeview State; you’ll do great!</p>
      <span class="signoff sibling">Love, CORWIN</span>
    </div>

    <div class="thumb-strip">
      <div class="thumb golf" role="img" aria-label="Tobin on a golf course carrying his golf bag"></div>
      <div class="thumb steps" role="img" aria-label="Tobin seated on stone steps in shirt and tie"></div>
      <div class="thumb soccer" role="img" aria-label="Young Tobin holding a soccer ball in a green jersey"></div>
      <div class="thumb flagwall" role="img" aria-label="Tobin standing before a flag mural wall beside a car"></div>
    </div>
  </main>
</body>
</html>
```